Bref créative
Business card and A5 "with our compliments" note
Verdalis - a service design company
I need double sided standard sized Business Card [3.5" x 2"]
Use whatever works
Bright & Fun-filled
Tom Brissel
Director
14 Korimu Street
Westmere Flats
Auckland 1047
NEW ZEALAND
tom@verdalis.co.nz
www.verdalis.co.nz
The business card should surprise: at first glance it should resemble something else. My business is about inquiry, research, and design e.g. a sticky note with ideas on it e.g. part of a questionnaire e.g. a card from a popular game like the "chance" card in Tradewind e.g. a jigsaw piece
Graphical rending as per comments OR expanded logo OR ....
Designers can remove the tagline if convenient, but the business card should then also say "service and programme design" somewhere

```html
<!DOCTYPE html>
<html lang="en">
<head>
<meta charset="utf-8">
<title>Verdalis – Business Card</title>
<link rel="stylesheet" href="https://fonts.googleapis.com/css2?family=Open+Sans:ital,wght@0,400;0,600;0,700;1,600&family=Tinos&display=swap">
<style>
  :root {
    --page: #ffffff;
    --card: #363435;
    --lime: #9bbe43;
    --forest: #1f6e3f;
    --ink-light: #ffffff;
  }
  html, body {
    margin: 0;
    padding: 0;
    width: 1200px;
    height: 726px;
    overflow: hidden;
    background: var(--page);
  }
  .sheet {
    position: relative;
    width: 1200px;
    height: 726px;
    font-family: "Open Sans", sans-serif;
    color: var(--ink-light);
  }
  .card {
    position: absolute;
    top: 0;
    width: 454px;
    height: 726px;
    background: var(--card);
    overflow: hidden;
  }
  .card--front { left: 0; }
  .card--back { left: 746px; }
  .card__corners {
    position: absolute;
    inset: 0;
    width: 100%;
    height: 100%;
  }
  .corner { fill: var(--lime); }

  /* Front */
  .brand-disc {
    position: absolute;
    left: 128px;
    top: 124px;
    width: 196px;
    height: 196px;
    border-radius: 50%;
    background: var(--forest);
  }
  .brand-name {
    position: absolute;
    left: 0;
    width: 454px;
    top: 344px;
    margin: 0;
    text-align: center;
    font-weight: 600;
    font-size: 58px;
    line-height: 1;
    letter-spacing: -1px;
    color: var(--ink-light);
  }
  .brand-tagline {
    position: absolute;
    right: 92px;
    top: 405px;
    margin: 0;
    font-weight: 600;
    font-style: italic;
    font-size: 15px;
    color: var(--ink-light);
  }
  .holder {
    position: absolute;
    left: 23px;
    top: 548px;
  }
  .holder__name {
    margin: 0;
    font-weight: 600;
    font-size: 32px;
    line-height: 1.1;
    padding-bottom: 4px;
    border-bottom: 3px solid var(--ink-light);
    width: 184px;
    white-space: nowrap;
  }
  .holder__role {
    margin: 9px 0 0;
    font-weight: 600;
    font-size: 21px;
  }

  /* Back */
  .back-disc {
    position: absolute;
    left: 41px;
    top: 140px;
    width: 384px;
    height: 384px;
    border-radius: 50%;
    background: var(--forest);
    opacity: 0.18;
  }
  .address {
    position: absolute;
    left: 31px;
    top: 434px;
    margin: 0;
    font-style: normal;
    font-size: 21px;
    line-height: 31px;
    letter-spacing: 0.3px;
  }
  .contact-list {
    position: absolute;
    left: 31px;
    top: 564px;
    margin: 0;
    padding: 0;
    list-style: none;
  }
  .contact {
    position: relative;
    padding-left: 36px;
    height: 33px;
    display: flex;
    align-items: center;
    font-size: 20px;
  }
  .contact__icon {
    position: absolute;
    left: 0;
    top: 50%;
    transform: translateY(-50%);
    width: 20px;
    height: 20px;
    fill: none;
    stroke: var(--ink-light);
    stroke-width: 1.6;
  }
  .contact--phone { font-weight: 700; font-size: 21px; }
  .contact--fax { font-size: 19px; }
  .contact--email { font-family: "Tinos", serif; font-size: 22px; }
  .contact__at {
    position: absolute;
    left: 0;
    font-family: "Open Sans", sans-serif;
    font-weight: 700;
    font-size: 19px;
  }
</style>
</head>
<body>
<main class="sheet">

  <section class="card card--front" aria-label="Business card front">
    <svg class="card__corners" viewBox="0 0 454 726" aria-hidden="true">
      <polygon class="corner" points="0,0 157,0 0,136"/>
      <polygon class="corner" points="454,589 454,726 295,726"/>
    </svg>
    <div class="brand-disc" aria-hidden="true"></div>
    <h1 class="brand-name">Verdalis</h1>
    <p class="brand-tagline">Service and programme design</p>
    <div class="holder">
      <h2 class="holder__name">Tom Brissel</h2>
      <p class="holder__role">Director</p>
    </div>
  </section>

  <section class="card card--back" aria-label="Business card back">
    <svg class="card__corners" viewBox="0 0 454 726" aria-hidden="true">
      <polygon class="corner" points="0,0 164,0 0,134"/>
      <polygon class="corner" points="454,590 454,726 293,726"/>
    </svg>
    <div class="back-disc" aria-hidden="true"></div>
    <address class="address">
      14 Korimu Street,<br>
      Westmere Flats<br>
      Auckland 1047<br>
      NEW ZEALAND
    </address>
    <ul class="contact-list">
      <li class="contact contact--phone">
        <svg class="contact__icon" viewBox="0 0 20 20" aria-hidden="true">
          <path d="M12 3 C8 5 5 11 5 17"/>
          <path d="M10 3.5 L13 2.5 M4 16 L6 18"/>
        </svg>
        +64 21 555 0186
      </li>
      <li class="contact contact--fax">
        <svg class="contact__icon" viewBox="0 0 20 20" aria-hidden="true">
          <rect x="3" y="10" width="14" height="5"/>
          <path d="M5 6 H15 M5 8 H15"/>
        </svg>
        xxxxxxxxxxxxxxx
      </li>
      <li class="contact contact--email">
        <span class="contact__at" aria-hidden="true">@</span>
        tom@verdalis.co.nz
      </li>
      <li class="contact contact--web">
        <svg class="contact__icon" viewBox="0 0 20 20" aria-hidden="true">
          <path d="M8 4 V16 M11 4 V16 M6 7 H13 M6 10 H13 M6 13 H13" stroke-width="1"/>
        </svg>
        www.verdalis.co.nz
      </li>
    </ul>
  </section>

</main>
</body>
</html>
```